Upscale business cards needed for family business

We need professional business cards created for several family members. We are a family business holding company. We would like these relatively simple and straightforward, but also with a unique element to set them apart. Probably stick with neutral and simple colors - white, grey etc. We need space for the traditional elements, including name, title, address, email/phone number. And we will be creating several from this template so it needs to be template that is easy to switch information in and out of.

Industry/Entity Type

Business

Contact Information for Business Card

Please include the attached Dunmore Ventures logo.

Requirements
Must have
• The attached Dunmore Ventures logo.

```html
<!DOCTYPE html>
<html lang="en">
<head>
<meta charset="utf-8">
<title>Dunmore Ventures – Business Card</title>
<link rel="stylesheet" href="https://fonts.googleapis.com/css2?family=Jost:wght@400;500;600&display=swap">
<style>
  :root {
    --backdrop: #d9dcdf;
    --card: #050505;
    --gold: #e8b21c;
    --white: #f4f4f4;
  }
  * { margin: 0; padding: 0; box-sizing: border-box; }
  html, body {
    width: 1200px;
    height: 675px;
    overflow: hidden;
    background: var(--backdrop);
    font-family: "Jost", Arial, sans-serif;
  }
  .card {
    position: absolute;
    left: 100px;
    top: 52px;
    width: 1000px;
    height: 571px;
    background: var(--card);
    box-shadow: 0 10px 30px rgba(0, 0, 0, 0.25);
  }
  .brand {
    position: absolute;
    left: 120px;
    top: 190px;
    display: flex;
    align-items: center;
    gap: 14px;
  }
  .brand-dot {
    width: 16px;
    height: 16px;
    border-radius: 50%;
    background: var(--gold);
  }
  .brand-name {
    font-size: 38px;
    font-weight: 500;
    letter-spacing: 3px;
    text-transform: uppercase;
    color: var(--white);
  }
  .identity {
    position: absolute;
    right: 440px;
    top: 330px;
    text-align: right;
  }
  .person-name {
    font-size: 34px;
    font-weight: 600;
    color: var(--gold);
    line-height: 1.1;
  }
  .person-title {
    font-size: 22px;
    font-weight: 400;
    color: var(--white);
    margin-top: 4px;
  }
  .divider {
    position: absolute;
    left: 578px;
    top: 300px;
    width: 1.5px;
    height: 150px;
    background: var(--gold);
  }
  .contacts {
    position: absolute;
    left: 600px;
    top: 300px;
    list-style: none;
    color: var(--white);
    font-size: 20px;
    line-height: 1.3;
  }
  .contact-item {
    display: flex;
    align-items: flex-start;
    gap: 12px;
    margin-bottom: 4px;
  }
  .contact-item.address { margin-top: 14px; }
  .contact-icon {
    flex: none;
    width: 18px;
    height: 18px;
    margin-top: 4px;
    fill: var(--gold);
  }
</style>
</head>
<body>
  <main class="card">
    <div class="brand">
      <span class="brand-dot"></span>
      <span class="brand-name">Dunmore Ventures</span>
    </div>

    <div class="identity">
      <p class="person-name">John Doe</p>
      <p class="person-title">Director</p>
    </div>

    <div class="divider"></div>

    <ul class="contacts">
      <li class="contact-item">
        <svg class="contact-icon" viewBox="0 0 24 24" aria-hidden="true"><path d="M6.6 10.8a15.2 15.2 0 0 0 6.6 6.6l2.2-2.2a1 1 0 0 1 1-.25 11.4 11.4 0 0 0 3.6.57 1 1 0 0 1 1 1V20a1 1 0 0 1-1 1A17 17 0 0 1 3 4a1 1 0 0 1 1-1h3.5a1 1 0 0 1 1 1c0 1.25.2 2.450.57 3.570a1 1 0 0 1-.25 1z"/></svg>
        <span>+01 555 210 4870</span>
      </li>
      <li class="contact-item">
        <svg class="contact-icon" viewBox="0 0 24 24" aria-hidden="true"><path d="M3 5h18a1 1 0 0 1 1 1v12a1 1 0 0 1-1 1H3a1 1 0 0 1-1-1V6a1 1 0 0 1 1-1zm1 2.3V17h16V7.3l-8 5.2z M4.6 7 12 11.8 19.4 7z"/></svg>
        <span>john@dunmoreventures.com</span>
      </li>
      <li class="contact-item address">
        <svg class="contact-icon" viewBox="0 0 24 24" aria-hidden="true"><path d="M12 2a7 7 0 0 0-7 7c0 5.2 7 13 7 13s7-7.8 7-13a7 7 0 0 0-7-7zm0 9.5A2.5 2.5 0 1 1 12 6.5a2.5 2.5 0 0 1 0 5z"/></svg>
        <span>48 Harbor Lane<br>Millbrook, Westland Region</span>
      </li>
    </ul>
  </main>
</body>
</html>
```